Surgery Office Letterhead Design

I'm seeking new letterhead that will comprise all of our office locations and logo and other applicable information, per the following:

Office Locations:

Bluewater Institute for Oral & Facial Surgery at Cleburne
347 Amberly Lane
Cleburne, Texas 76058
Phone 817.392.4806
Fax 817.392.7734

Bluewater Institute for Oral & Facial Surgery at Stephenville
588 Quarry Hollow Parkway
Stephenville, Texas 76428
Phone 254.763.2248
Fax 254.763.2251

Bluewater Institute for Oral & Facial Surgery at Belton
715 West 9th Street
Belton, Texas 76537
Phone 254.481.6072
Fax 254.481.6079

Other Info to include:

www.bluewatermaxillo.example
hello@bluewatermaxillo.example

Industry/Entity Type

Medical

Font styles to use
Serif
Sans Serif

Requirements
Must have
• See Project Description

```html
<!DOCTYPE html>
<html lang="en">
<head>
<meta charset="utf-8">
<title>Bluewater Institute Letterhead</title>
<link rel="stylesheet" href="https://fonts.googleapis.com/css2?family=Cinzel:wght@400;600;700&display=swap">
<style>
  :root {
    --navy: #1c3a78;
    --navy-deep: #17336b;
    --band-light: #3a72b4;
    --paper: #ffffff;
    --ghost: #f1f3f8;
    --backdrop: #ffffff;
    --on-band: #ffffff;
  }
  html, body {
    margin: 0;
    padding: 0;
    width: 901px;
    height: 1200px;
    overflow: hidden;
    background: var(--backdrop);
  }
  .letterhead {
    position: relative;
    width: 901px;
    height: 1200px;
    background: var(--paper);
    overflow: hidden;
    font-family: "Cinzel", serif;
  }
  .brand {
    position: absolute;
    left: 66px;
    top: 80px;
    display: flex;
    align-items: center;
    gap: 12px;
  }
  .brand-dot {
    width: 30px;
    height: 30px;
    border-radius: 50%;
    background: var(--navy);
  }
  .brand-name {
    font-weight: 600;
    font-size: 27px;
    line-height: 1;
    color: var(--navy);
    letter-spacing: 0.5px;
  }
  .practice-title {
    position: absolute;
    top: 168px;
    left: 0;
    width: 928px;
    margin: 0;
    text-align: center;
    font-weight: 600;
    font-size: 22px;
    color: var(--navy);
    letter-spacing: 0.3px;
  }
  .ghost-emblem {
    position: absolute;
    left: 290px;
    top: 330px;
    width: 330px;
    height: 560px;
  }
  .footer-band {
    position: absolute;
    left: 0;
    bottom: 0;
    width: 901px;
    height: 200px;
  }
  .office-list {
    position: absolute;
    left: 40px;
    top: 1088px;
    width: 821px;
    display: grid;
    grid-template-columns: repeat(3, 1fr);
    color: var(--on-band);
    text-align: center;
  }
  .office {
    margin: 0;
    font-style: normal;
    font-size: 10px;
    font-weight: 400;
    line-height: 13px;
  }
  .office-name {
    display: block;
    font-size: 12px;
    font-weight: 700;
    line-height: 16px;
  }
  .footer-contact {
    position: absolute;
    left: 0;
    top: 1166px;
    width: 901px;
    display: flex;
    justify-content: center;
    align-items: center;
    gap: 6px;
    white-space: nowrap;
    color: var(--on-band);
    font-size: 11px;
    font-weight: 700;
  }
  .footer-contact svg {
    width: 11px;
    height: 11px;
  }
  .footer-contact .spacer { width: 14px; }
</style>
</head>
<body>
<main class="letterhead">
  <div class="brand">
    <span class="brand-dot"></span>
    <span class="brand-name">Bluewater Institute</span>
  </div>

  <h1 class="practice-title">Bluewater Institute for Oral &amp; Facial Surgery</h1>

  <svg class="ghost-emblem" viewBox="0 0 330 560" aria-hidden="true">
    <circle cx="165" cy="280" r="160" fill="var(--ghost)"/>
  </svg>

  <svg class="footer-band" viewBox="0 0 901 200" preserveAspectRatio="none" aria-hidden="true">
    <defs>
      <linearGradient id="bandGradient" x1="0" y1="0" x2="1" y2="0">
        <stop offset="0" stop-color="var(--navy-deep)"/>
        <stop offset="0.5" stop-color="var(--band-light)"/>
        <stop offset="1" stop-color="var(--navy-deep)"/>
      </linearGradient>
    </defs>
    <path d="M0,8 C200,50 480,66 901,54 L901,200 L0,200 Z" fill="var(--navy-deep)"/>
    <path d="M0,58 C250,82 560,44 901,62 L901,200 L0,200 Z" fill="#ffffff"/>
    <path d="M0,66 C250,90 560,52 901,70 L901,200 L0,200 Z" fill="url(#bandGradient)"/>
  </svg>

  <div class="office-list">
    <address class="office">
      <span class="office-name">Cleburne</span>
      347 Amberly Lane<br>
      Cleburne, Texas 76058<br>
      Phone 817.392.4806 · Fax 817.392.7734
    </address>
    <address class="office">
      <span class="office-name">Stephenville</span>
      588 Quarry Hollow Parkway<br>
      Stephenville, Texas 76428<br>
      Phone 254.763.2248 · Fax 254.763.2251
    </address>
    <address class="office">
      <span class="office-name">Belton</span>
      715 West 9th Street<br>
      Belton, Texas 76537<br>
      Phone 254.481.6072 · Fax 254.481.6079
    </address>
  </div>

  <div class="footer-contact">
    <svg viewBox="0 0 12 12" aria-hidden="true"><circle cx="6" cy="6" r="5" fill="none" stroke="#fff" stroke-width="1.2"/><path d="M1 6 H11 M6 1 C3.5 3.5 3.5 8.5 6 11 M6 1 C8.5 3.5 8.5 8.5 6 11" fill="none" stroke="#fff" stroke-width="1"/></svg>
    <span>www.bluewatermaxillo.example</span>
    <span class="spacer"></span>
    <svg viewBox="0 0 12 12" aria-hidden="true"><rect x="1" y="2.5" width="10" height="7" fill="none" stroke="#fff" stroke-width="1.2"/><path d="M1 2.5 L6 6.5 L11 2.5" fill="none" stroke="#fff" stroke-width="1.1"/></svg>
    <span>hello@bluewatermaxillo.example</span>
  </div>
</main>
</body>
</html>
```